A5 Flyer Design Double Sided for a Onsite Technology company that comes to you

*** Updated Breif now ***

We made a decission that we would like a double sided A5 Flyer that is for Technology only, we will load up another for Telco later on.

Some ideas below for what we after

We want to make sure the flyer is nice looking, Attached is current business card design. I like to contuine with that flow.

Details to have on there are, Our Phone Number 02 4872 6190, our website: quorvane.com.au and our ABN number

I want to not have pricing on this more a direction that we the Computer Repair Store that comes to you.

listing our services we provide.

have updated the breif

Target Market(s)

Home, Retirment Villages and Small Business's

Requirements
Should not have
• Bright Colours

```html
<!DOCTYPE html>
<html lang="en">
<head>
<meta charset="utf-8">
<title>Quorvane – Onsite Technology Flyer</title>
<link href="https://fonts.googleapis.com/css2?family=Montserrat:wght@400;500&family=Plus+Jakarta+Sans:wght@500;800&display=swap" rel="stylesheet">
<style>
  :root {
    --teal-deep: #07363a;
    --teal-glow: #0b5d6a;
    --green: #149a48;
    --orange: #f06225;
    --orange-muted: #d45a28;
    --white: #ffffff;
    --skin-light: #c9a27c;
    --skin-dark: #5a3a24;
    --page: #ffffff;
  }
  * { box-sizing: border-box; margin: 0; padding: 0; }
  html, body { width: 1200px; height: 1082px; overflow: hidden; background: var(--page); }
  .canvas { position: relative; width: 1200px; height: 1082px; }

  .flyer {
    position: absolute; top: 174px; width: 520px; height: 727px;
    border-radius: 15px; overflow: hidden;
    background:
      radial-gradient(ellipse 300px 320px at 0% 78%, var(--teal-glow) 0%, rgba(11,93,106,0) 100%),
      var(--teal-deep);
    color: var(--white);
    font-family: "Montserrat", sans-serif;
  }
  .flyer--front { left: 63px; }
  .flyer--back { left: 609px; }

  .decor { position: absolute; inset: 0; width: 520px; height: 727px; }

  .brand { position: absolute; left: 45px; top: 38px; height: 56px; display: flex; align-items: center; gap: 12px; }
  .brand__dot { width: 56px; height: 56px; border-radius: 50%; background: var(--orange); flex: none; }
  .brand__name {
    white-space: nowrap;
    font-family: "Montserrat", sans-serif; font-weight: 500; font-size: 24px; line-height: 1;
    color: var(--orange);
  }

  .headline__intro { position: absolute; left: 43px; top: 134px; font-size: 28px; line-height: 1; }
  .headline__key {
    position: absolute; left: 40px; top: 160px;
    font-family: "Plus Jakarta Sans", sans-serif; font-weight: 800; font-size: 58px; line-height: 1; letter-spacing: -1px;
  }
  .headline__rest { position: absolute; left: 43px; top: 224px; font-size: 26px; line-height: 31px; }
  .intro { position: absolute; left: 43px; top: 319px; font-size: 15px; line-height: 19px; white-space: nowrap; }

  .callout {
    position: absolute; left: 21px; top: 395px; width: 257px; height: 109px;
    background: var(--orange-muted);
    border-radius: 0 35px 0 35px;
    padding: 24px 0 0 20px;
    font-size: 13.5px; line-height: 19.5px;
  }

  .portrait {
    position: absolute; left: 356px; top: 300px; width: 164px; height: 427px;
    border-radius: 90px 0 0 0;
    background: linear-gradient(170deg, var(--skin-dark) 0%, #7a5234 40%, var(--skin-light) 100%);
  }

  .contact { position: absolute; left: 40px; top: 610px; }
  .flyer--back .contact { left: 74px; top: 608px; }
  .contact__title {
    font-family: "Plus Jakarta Sans", sans-serif; font-weight: 800; font-size: 25px; line-height: 1; letter-spacing: -0.5px;
  }
  .contact__phone { display: flex; align-items: center; gap: 6px; margin-top: 8px; font-size: 12px; line-height: 14px; padding-left: 2px; }
  .contact__icon { width: 13px; height: 13px; }
  .contact__web { margin-top: 3px; font-size: 12px; line-height: 14px; padding-left: 2px; }

  .services__title {
    position: absolute; left: 103px; top: 190px;
    font-family: "Plus Jakarta Sans", sans-serif; font-weight: 800; font-size: 31px; line-height: 1; letter-spacing: -0.5px;
  }
  .services__list {
    position: absolute; left: 102px; top: 254px; list-style: none;
    font-family: "Plus Jakarta Sans", sans-serif; font-weight: 500; font-size: 16px; line-height: 30.2px;
  }
  .services__list li { display: flex; align-items: center; gap: 11px; white-space: nowrap; }
  .services__tick { width: 16px; height: 12px; flex: none; }
</style>
</head>
<body>
<main class="canvas">

  <section class="flyer flyer--front">
    <svg class="decor" viewBox="0 0 520 727" aria-hidden="true">
      <circle cx="646" cy="-85" r="271" fill="none" stroke="var(--green)" stroke-width="43"/>
      <polygon points="0,694 520,724 520,727 0,727" fill="var(--orange-muted)"/>
    </svg>

    <div class="portrait" role="img" aria-label="Smiling woman with curly hair pointing towards the message"></div>

    <div class="brand">
      <span class="brand__dot"></span>
      <span class="brand__name">Quorvane</span>
    </div>

    <p class="headline__intro">Are you</p>
    <h1 class="headline__key">Struggling</h1>
    <p class="headline__rest">with your computer,<br>Internet Or Devices?</p>

    <p class="intro">We Are The Local Central Coast<br>Tech Team That Brings Support To You!</p>

    <div class="callout">No Need To Leave Your Home<br>Or Office We’ll Take Care Of<br>Everithing Right Where You Are</div>

    <div class="contact">
      <p class="contact__title">Call us today</p>
      <p class="contact__phone">
        <svg class="contact__icon" viewBox="0 0 24 24" aria-hidden="true"><circle cx="12" cy="12" r="12" fill="var(--white)"/><path d="M8.2 6.5l1.8-.4 1.2 2.8-1.3 1c.7 1.5 1.8 2.6 3.3 3.3l1-1.3 2.8 1.2-.4 1.8c-.2.6-.8 1-1.4.9-4-.5-7.3-3.8-7.8-7.8-.1-.7.3-1.3.8-1.5z" fill="var(--teal-deep)"/></svg>
        02 4872 6190
      </p>
      <p class="contact__web">quorvane.com.au</p>
    </div>
  </section>

  <section class="flyer flyer--back">
    <svg class="decor" viewBox="0 0 520 727" aria-hidden="true">
      <circle cx="646" cy="-85" r="271" fill="none" stroke="var(--green)" stroke-width="43"/>
      <polygon points="0,694 520,724 520,727 0,727" fill="var(--orange-muted)"/>
      <path d="M107,156 H409 Q444,156 444,191 V425 Q444,445 428,457 L290,568 Q275,589 250,589 H107 Q72,589 72,554 V191 Q72,156 107,156 Z" fill="var(--orange)"/>
      <path d="M89,500 A72,72 0 0 1 161,572" fill="none" stroke="var(--green)" stroke-width="24"/>
    </svg>

    <div class="brand">
      <span class="brand__dot"></span>
      <span class="brand__name">Quorvane</span>
    </div>

    <h2 class="services__title">Our Service :</h2>
    <ul class="services__list">
      <li><svg class="services__tick" viewBox="0 0 16 12" aria-hidden="true"><path d="M1 6.5l4.5 4L15 1" fill="none" stroke="var(--white)" stroke-width="2"/></svg>Onsite Home and/or Office Visits</li>
      <li><svg class="services__tick" viewBox="0 0 16 12" aria-hidden="true"><path d="M1 6.5l4.5 4L15 1" fill="none" stroke="var(--white)" stroke-width="2"/></svg>Data Backup &amp; Cyber Security</li>
      <li><svg class="services__tick" viewBox="0 0 16 12" aria-hidden="true"><path d="M1 6.5l4.5 4L15 1" fill="none" stroke="var(--white)" stroke-width="2"/></svg>Smart Home &amp; Office Technology</li>
      <li><svg class="services__tick" viewBox="0 0 16 12" aria-hidden="true"><path d="M1 6.5l4.5 4L15 1" fill="none" stroke="var(--white)" stroke-width="2"/></svg>Wi-Fi Installation &amp; Troubleshooting</li>
      <li><svg class="services__tick" viewBox="0 0 16 12" aria-hidden="true"><path d="M1 6.5l4.5 4L15 1" fill="none" stroke="var(--white)" stroke-width="2"/></svg>Network Setup &amp; Optimisation</li>
      <li><svg class="services__tick" viewBox="0 0 16 12" aria-hidden="true"><path d="M1 6.5l4.5 4L15 1" fill="none" stroke="var(--white)" stroke-width="2"/></svg>Supply of New Computer &amp; Hardware</li>
    </ul>

    <div class="contact">
      <p class="contact__title">Call us today</p>
      <p class="contact__phone">
        <svg class="contact__icon" viewBox="0 0 24 24" aria-hidden="true"><circle cx="12" cy="12" r="12" fill="var(--white)"/><path d="M8.2 6.5l1.8-.4 1.2 2.8-1.3 1c.7 1.5 1.8 2.6 3.3 3.3l1-1.3 2.8 1.2-.4 1.8c-.2.6-.8 1-1.4.9-4-.5-7.3-3.8-7.8-7.8-.1-.7.3-1.3.8-1.5z" fill="var(--teal-deep)"/></svg>
        02 4872 6190
      </p>
      <p class="contact__web">quorvane.com.au</p>
    </div>
  </section>

</main>
</body>
</html>
```